Hair Extension Aftercare sheet

This sheet is to give to customers regarding the aftercare of hair extensions. There should be Simple and minimal look - approx A5 size and can be folded to suit. I have attached the content and logo files for use.
We are not looking for to much artwork just clean, professional look.
All the content provided in a compact flyer format i.e
A foldable A5 pamphlet or the like, this is for packaging requirements
Please do not submit A4 layouts

Industry/Entity Type

Hair And Beauty

Requirements
Must have
• All the content provided in a compact flyer format i.e
• A foldable A5 pamphlet or the like, this is for packaging requirements
Should not have
• tacky art work or images - must be clean lines

```html
<!DOCTYPE html>
<html lang="en">
<head>
<meta charset="utf-8">
<title>Aftercare and Maintenance Guidelines</title>
<link href="https://fonts.googleapis.com/css2?family=Tinos:wght@400;700&family=Montserrat:wght@600;700&display=swap" rel="stylesheet">
<style>
  :root {
    --backdrop: #d3d4d6;
    --paper: #ffffff;
    --band: #a6a7a9;
    --band-text: #ffffff;
    --heading: #5f6062;
    --heading-strong: #4a4b4d;
    --body: #231f20;
    --alert: #e5202a;
    --fold: #b9babc;
  }
  * { box-sizing: border-box; margin: 0; padding: 0; }
  html, body { width: 1200px; height: 720px; overflow: hidden; background: var(--backdrop); }
  .spread {
    position: absolute; left: 150px; top: 42px; width: 902px; height: 633px;
    background: var(--paper); border: 1px solid #9c9d9f;
    box-shadow: 0 2px 6px rgba(0,0,0,.12);
  }
  .header-band {
    position: absolute; left: 0; top: 0; width: 100%; height: 30px;
    background: var(--band);
  }
  .header-title {
    position: absolute; left: 42px; top: 10px;
    font: 700 10.5px/1 "Montserrat", sans-serif; letter-spacing: 3.9px;
    color: var(--band-text); text-transform: uppercase;
  }
  .brand {
    position: absolute; right: 14px; top: 9px; display: flex; align-items: center; gap: 5px;
    font: 700 10px/1 "Montserrat", sans-serif; color: var(--band-text); letter-spacing: .5px;
  }
  .brand-square { width: 9px; height: 9px; background: var(--band-text); }
  .fold { position: absolute; left: 450px; top: 0; width: 1px; height: 100%; background: var(--fold); }
  .page {
    position: absolute; width: 367px;
    font: 400 11px/13.6px "Tinos", "Times New Roman", serif; color: var(--body);
  }
  .page-left { left: 42px; top: 59px; }
  .page-right { left: 492px; top: 60px; }
  .page p { text-align: justify; margin-bottom: 5.5px; }
  .page h3 {
    font: 700 10px/13px "Montserrat", sans-serif; color: var(--heading);
    margin: 1px 0 6px;
  }
  .page h3.important { color: var(--heading-strong); }
  .page-right h3:first-child { margin-top: 0; }
  .alert { color: var(--alert); }
  .alert strong { font-weight: 700; }
  .warning { color: var(--alert); text-transform: uppercase; }
</style>
</head>
<body>
<main class="spread">
  <div class="header-band">
    <span class="header-title">Aftercare and Maintenance Guidelines</span>
    <span class="brand"><span class="brand-square"></span>Lumen Hair</span>
  </div>
  <div class="fold"></div>

  <section class="page page-left">
    <p>apply the shampoo for a second time. There is no need to apply a lot of shampoo in the lengths. The hair will get cleaned when you rinse the hair out (unless extremely dirty).</p>
    <p class="alert"><strong>Avoid:</strong> Shampoos that contain sulphates &amp; products that are oil based.</p>
    <p>If you can't wash it off your hands without shampoo, it is more likely oil based.</p>
    <h3>After you washed the hair:</h3>
    <p>After washing you may use a conditioner however, apply the conditioner from the ends to half way up the length. Never at the roots. Comb the conditioner through using a large wide tooth comb until all tangles are removed. Rinse thoroughly to leave no residue in the hair. Towel dry the hair by squeezing it with the towel. Don't rub or massage the hair.</p>
    <p>You can apply small amounts of leave-in conditioner or a recommended styling product, comb through with your fingers into the direction you would like your hair to fall and scruntch it upwards once more. After you have done this leave the hair to dry completely without touching, combing or brushing it. = Best natural result.</p>
    <p>Let it dry naturally or use your favourite styling equipment. Use leave in conditioners only at the ends! When the hair is completely dry.</p>
    <h3>At Night</h3>
    <p>Braid the hair in a large loose braid at the nape of the neck before going to sleep. Do not sleep with wet hair, this will cause tangling and will make it difficult to style the following morning.</p>
    <h3>Styling the hair</h3>
    <p>You can use a ceramic straightening iron or a hair dryer with a bristle brush to smooth the hair. Other styling tools that can be used are: Heated rollers, steam rollers, curling irons, hot air curling tongs and setting rollers.</p>
    <h3 class="important">IMPORTANT:</h3>
    <p class="warning">Never use hot styling equipment that exceeds 200 degrees celsius or 392 degrees fahrenheit.</p>
    <p>Temperatures above this can damage the protein in the hair causing it to solidify and make the hair dry and unmanageable. Always keep hot styling equipment moving through the hair and do not hold for too long in one place. We do not recommend using straightening irons on wet hair.</p>
  </section>

  <section class="page page-right">
    <h3>Sports and other activities</h3>
    <p>Don't expose your hair to strong windy conditions like sailing, motor sports, cabriolet cars. Wear protective head wear. If you sweat a lot during work outs, at least rinse out the saltiness as this will dry out the hair.</p>
    <h3>Visiting Saunas and steam rooms</h3>
    <p>Braid the hair in a loose braid in the nape of the neck and put it up using a hair clip. The hair can get very hot and can be painful when it touches the skin just like your own natural hair. Only brush the hair when it is cooled down. After the sauna rinse the hair under the shower and preferably wash the hair and condition it at the end of the visit or when you get home as stated in this aftercare sheet.</p>
    <h3>Swimming</h3>
    <p>It is not recommended that you swim while wearing curly, deep curly and deep curl textures, you can swim but don't submerge your head in the water. If you swim every day or frequently, other textures are more suitable. Other textures before swimming, brush out any tangles. Make one braid at the nape of your neck. Try to keep your hair out of the water as much as possible.</p>
    <p>After swimming in chlorinated water or sea water, undo the braid and rinse immediately under the shower. This is very important to rinse out all of the chlorine or salt, both will dry your hair out when you leave it in for too long. Condition and comb out with a wide tooth comb, then leave to dry naturally. Wash and condition the hair as soon as possible as recommended in this guide.</p>
    <h3>Sunbathing</h3>
    <p>Braid your hair in a large braid at the back of the neck. After sunbathing, do not undo the braid until the hair cools down.</p>
    <h3>Tanning machines</h3>
    <p>Whilst laying under a tanning machine, cover the hair loosely with a towel. Don't apply skin tan oil or sunblock to the hair.</p>
    <h3>General Daily Styling Guide</h3>
    <p>In the morning undo the braid and brush the hair starting from the ends upwards to the roots until all tangles are removed. If necessary, dampen the hair with a water spray. You can use a ceramic hair straightening iron (NOT ON DAMP OR WET HAIR) or a hair dryer with an extension brush</p>
  </section>
</main>
</body>
</html>
```